Business Card Design Project

We would need a business name card for our online website business, http://www.brindle.com.sg/. We would need to include our website on the name card as well.

Target Market(s)

Adults and kids in Singapore, mainly expatriates

Industry/Entity Type

Business

Font styles to use
Sans Serif

Colors

Designer to choose colors to be used in the design.

Requirements
Must have
• Must include our "vorn" logo and we would like our name card to be printed on light craft paper material

```html
<!DOCTYPE html>
<html lang="en">
<head>
<meta charset="utf-8">
<title>Vorn business card</title>
<link rel="stylesheet" href="https://fonts.googleapis.com/css2?family=Open+Sans:wght@400;700&display=swap">
<style>
  :root {
    --backdrop: #d9d4cc;
    --paper: #ebe5da;
    --paper-edge: #d6cfc2;
    --navy: #3b3f7c;
    --red: #e0443e;
    --ink: #3a3a3a;
    --rule: #2e2e2e;
  }
  * { margin: 0; padding: 0; box-sizing: border-box; }
  html, body { width: 1200px; height: 1023px; overflow: hidden; }
  body {
    background: var(--backdrop);
    font-family: "Open Sans", Arial, sans-serif;
    color: var(--ink);
    position: relative;
  }
  .card {
    position: absolute;
    top: 357px;
    width: 520px;
    height: 310px;
    background: var(--paper);
    border: 1px solid var(--paper-edge);
    box-shadow: 0 6px 16px rgba(0,0,0,.18);
    overflow: hidden;
  }
  .card--front { left: 50px; }
  .card--back { left: 630px; }

  .accent-bar {
    position: absolute; top: 0; right: 28px;
    width: 18px; height: 70px; background: var(--red);
  }
  .brand {
    position: absolute;
    font-weight: 700; color: var(--navy); letter-spacing: 3px;
    white-space: nowrap;
  }
  .card--front .brand {
    left: 0; width: 250px; top: 180px;
    text-align: center; font-size: 34px; line-height: 44px;
  }

  .details { position: absolute; left: 250px; top: 58px; width: 240px; }
  .details__name {
    font-size: 21px; font-weight: 700; color: var(--red); margin-bottom: 14px;
  }
  .contact { list-style: none; }
  .contact__item {
    display: flex; align-items: center; gap: 10px;
    font-size: 13px; line-height: 24px;
  }
  .icon { width: 14px; height: 14px; flex: none; }
  .details__rule { height: 1px; background: var(--rule); margin: 16px 0 14px; }
  .address { display: flex; align-items: flex-start; gap: 10px; font-size: 13px; line-height: 19px; font-style: normal; }
  .address .icon { width: 22px; height: 22px; margin-top: 3px; }

  .card--back .brand {
    left: 0; right: 0; top: 0; bottom: 0;
    display: flex; align-items: center; justify-content: center;
    font-size: 58px; letter-spacing: 6px;
  }
</style>
</head>
<body>
  <section class="card card--front">
    <div class="accent-bar"></div>
    <div class="brand">VORN</div>
    <div class="details">
      <p class="details__name">Mara Tan</p>
      <ul class="contact">
        <li class="contact__item">
          <svg class="icon" viewBox="0 0 14 14"><circle cx="7" cy="7" r="6" fill="none" stroke="var(--navy)"/><path d="M5 4l1.2 1.6-.8.8c.5 1 1.2 1.7 2.2 2.2l.8-.8L10 9l-.8 1C6.5 9.8 4.2 7.5 4 4.8z" fill="var(--navy)"/></svg>
          <span>6310 4582</span>
        </li>
        <li class="contact__item">
          <svg class="icon" viewBox="0 0 14 14"><circle cx="7" cy="7" r="6" fill="none" stroke="var(--navy)"/><rect x="4" y="5" width="6" height="4.4" fill="none" stroke="var(--navy)" stroke-width=".9"/><path d="M4 5l3 2.4L10 5" fill="none" stroke="var(--navy)" stroke-width=".9"/></svg>
          <span>email@vorncorp.com</span>
        </li>
        <li class="contact__item">
          <svg class="icon" viewBox="0 0 14 14"><circle cx="7" cy="7" r="6" fill="none" stroke="var(--navy)"/><circle cx="7" cy="7" r="3.2" fill="none" stroke="var(--navy)" stroke-width=".9"/><path d="M3.8 7h6.4M7 3.8v6.4" stroke="var(--navy)" stroke-width=".8"/></svg>
          <span>www.brindle.com.sg</span>
        </li>
      </ul>
      <div class="details__rule"></div>
      <address class="address">
        <svg class="icon" viewBox="0 0 22 22"><circle cx="11" cy="11" r="10" fill="none" stroke="var(--navy)" stroke-width="1.3"/><path d="M11 5.5a3.3 3.3 0 0 0-3.3 3.3c0 2.5 3.3 6.4 3.3 6.4s3.3-3.9 3.3-6.4A3.3 3.3 0 0 0 11 5.5z" fill="var(--navy)"/><circle cx="11" cy="8.8" r="1.2" fill="var(--paper)"/></svg>
        <span>8 Harbour Lane<br>#09-11 Singapore 048620</span>
      </address>
    </div>
  </section>

  <section class="card card--back">
    <div class="brand">VORN</div>
  </section>
</body>
</html>
```